Company Mission & Values Poster

I'd like an A2 Portrait Poster displaying our company's Mission & Values.
See our website for our logo, fonts, mission & values.
https://valtemo.com.au/

Our Mission: Creating homes for abundant life
Values: Love, Thinking, Team, Zoe.

Some ideas to consider:
Mission as the Headline then
A logo for each of the 4 Values and the words

Target Market(s)

Myself & my team

Industry/Entity Type

Real Estate

Font styles to use
Other font styles liked:
• Company fonts as seen on our website

```html
<!DOCTYPE html>
<html lang="en">
<head>
<meta charset="utf-8">
<title>Valtemo — Mission &amp; Values</title>
<link href="https://fonts.googleapis.com/css2?family=Playfair+Display:wght@700;800&family=Poppins:wght@400&display=swap" rel="stylesheet">
<style>
  :root {
    --ink: #07362e;
    --paper: #ffffff;
  }
  * { margin: 0; padding: 0; box-sizing: border-box; }
  html, body { width: 849px; height: 1200px; overflow: hidden; background: var(--paper); }
  .poster {
    position: relative;
    width: 849px;
    height: 1200px;
    background: var(--paper);
    color: var(--ink);
    font-family: "Poppins", sans-serif;
  }
  .mission {
    position: absolute;
    left: 0; right: 0;
    text-align: center;
    font-family: "Playfair Display", serif;
    font-weight: 800;
    line-height: 1;
  }
  .mission__lead { top: 80px; font-size: 100px; letter-spacing: -0.01em; }
  .mission__key { top: 172px; font-size: 138px; letter-spacing: 0.01em; }
  .mission__tail { top: 300px; font-size: 49px; font-weight: 700; letter-spacing: -0.005em; }

  .value {
    position: absolute;
    left: 137px;
    width: 571px;
    text-align: center;
  }
  .value__head {
    display: flex;
    align-items: center;
    gap: 10px;
    height: 36px;
  }
  .value__rule {
    flex: 1;
    height: 1px;
    background: var(--ink);
    position: relative;
  }
  .value__rule::after {
    content: "";
    position: absolute;
    top: -2px;
    width: 5px; height: 5px;
    border-radius: 50%;
    background: var(--ink);
  }
  .value__rule--left::after { right: -2px; }
  .value__rule--right::after { left: -2px; }
  .value__title {
    font-family: "Playfair Display", serif;
    font-weight: 700;
    font-size: 35px;
    line-height: 1;
    letter-spacing: 0.01em;
  }
  .value__text {
    margin-left: -40px;
    margin-right: -40px;
    margin-top: 5px;
    font-size: 17.2px;
    line-height: 30.5px;
  }

  .value--love { top: 414px; }
  .value--thinking { top: 558px; }
  .value--team { top: 702px; }
  .value--zoe { top: 848px; }

  .brand {
    position: absolute;
    top: 1040px;
    left: 0; right: 0;
    display: flex;
    justify-content: center;
    align-items: center;
    gap: 26px;
  }
  .brand__mark {
    width: 50px; height: 50px;
    border: 2px solid var(--ink);
    border-radius: 50%;
  }
  .brand__name {
    font-family: "Playfair Display", serif;
    font-weight: 700;
    font-size: 52px;
    letter-spacing: 0.16em;
    line-height: 1;
  }
</style>
</head>
<body>
<main class="poster">
  <h1>
    <span class="mission mission__lead">CREATING</span>
    <span class="mission mission__key">HOMES</span>
    <span class="mission mission__tail">FOR ABUNDANT LIFE</span>
  </h1>

  <section class="value value--love">
    <div class="value__head"><span class="value__rule value__rule--left"></span><h2 class="value__title">LOVE</h2><span class="value__rule value__rule--right"></span></div>
    <p class="value__text">Our mission is founded in our love and respect for people -<br>those we develop for, those in our teams and those in the<br>communities we create and operate within.</p>
  </section>

  <section class="value value--thinking">
    <div class="value__head"><span class="value__rule value__rule--left"></span><h2 class="value__title">THINKING</h2><span class="value__rule value__rule--right"></span></div>
    <p class="value__text">We believe in the power of thinking. Our rigorous and creative<br>processes create beautifully considered solutions for our purchasers,<br>the communities we develop within and the environment.</p>
  </section>

  <section class="value value--team">
    <div class="value__head"><span class="value__rule value__rule--left"></span><h2 class="value__title">TEAM</h2><span class="value__rule value__rule--right"></span></div>
    <p class="value__text">Property development is a team sport. We surround ourselves<br>with the best designers and advisers. We strive to create an environment<br>that allows them to do their best work and love doing it.</p>
  </section>

  <section class="value value--zoe">
    <div class="value__head"><span class="value__rule value__rule--left"></span><h2 class="value__title">ZOE</h2><span class="value__rule value__rule--right"></span></div>
    <p class="value__text">Our mission is to create places for ‘Zoe’<br>the Greek word for abundant life. We do this through exquisite design,<br>quality construction and celebrating nature.</p>
  </section>

  <footer class="brand">
    <span class="brand__mark"></span>
    <span class="brand__name">VALTEMO</span>
  </footer>
</main>
</body>
</html>
```